Business Card for Bright Furrow Lawn & Landscape

Double Sided Card Design - I think one side of the card should be cleaner, with logo, contact info, and "Complete Residential & Commercial Landscape Services", and on the other side it should list the services we offer:

- Lawn Care & Mowing
- Hedge & Shrub Trimming
- Leaf Removal & Clean Up
- Aeration & Sod
- Mulch & Rock Installations
- Landscape Installations & Renovations
- Commercial Snow Removal

Please make it clean and very professional... don't want it too be too busy, but want to tell them what we do.

Target Market(s)

Residential and Commercial

Industry/Entity Type

Landscape

Contact Information for Business Card

Fully Insured
Dale Ostrov
410-372-6184
Dostrov07@quillpost.net

Requirements
Must have
• Double Sided, Cleaner on one side, more information and text on the other side.

```html
<!DOCTYPE html>
<html lang="en">
<head>
<meta charset="utf-8">
<title>Bright Furrow Lawn &amp; Landscape – Business Card</title>
<link rel="stylesheet" href="https://fonts.googleapis.com/css2?family=Arimo:wght@400;700&family=Cinzel:wght@600&display=swap">
<style>
  :root {
    --backdrop: #eeebe6;
    --card: #ffffff;
    --leaf: #8cc63f;
    --leaf-deep: #77b02a;
    --lime-band: #c5e05a;
    --sun-band: #e8ea3a;
    --pale-band: #dcebb0;
    --ink-green: #7aa52a;
    --text-light: #ffffff;
  }
  * { margin: 0; padding: 0; box-sizing: border-box; }
  html, body {
    width: 1200px; height: 992px; overflow: hidden;
    background: var(--backdrop);
  }
  .canvas { position: relative; width: 1200px; height: 992px; }
  .card {
    position: absolute; left: 225px; width: 488px; height: 316px;
    background: var(--card); overflow: hidden;
    box-shadow: 0 6px 14px rgba(0,0,0,0.18);
  }
  .card--front { top: 147px; }
  .card--back { top: 536px; }
  .card__art { position: absolute; inset: 0; width: 100%; height: 100%; }

  .brand {
    position: absolute; left: 26px; top: 86px; width: 230px;
    text-align: center; color: var(--ink-green);
    font-family: "Cinzel", serif; font-weight: 600; white-space: nowrap;
  }
  .brand__dot {
    display: block; width: 56px; height: 56px; margin: 0 auto 12px;
    border-radius: 50%; background: var(--leaf);
  }
  .brand__name { display: block; font-size: 19px; line-height: 1.1; letter-spacing: 0.4px; }
  .brand__tag { display: block; font-size: 11px; letter-spacing: 1.8px; margin-top: 3px; }

  .contact {
    position: absolute; left: 330px; top: 200px; list-style: none;
    font-family: "Arimo", sans-serif; font-weight: 700; font-size: 12.5px;
    line-height: 18.5px; color: var(--text-light); white-space: nowrap;
  }
  .contact__web { font-size: 12px; letter-spacing: 0.8px; margin-left: -11px; }

  .services {
    position: absolute; left: 300px; top: 128px;
    font-family: "Arimo", sans-serif; color: var(--ink-green);
  }
  .services__title { font-size: 12.5px; font-weight: 400; margin-bottom: 18px; }
  .services__list { list-style: none; font-size: 11.5px; line-height: 17px; }
  .services__list li { padding-left: 9px; text-indent: -9px; }
  .services__list li::before { content: "- "; }
</style>
</head>
<body>
<main class="canvas">

  <section class="card card--front" aria-label="Business card front">
    <svg class="card__art" viewBox="0 0 488 316" preserveAspectRatio="none" aria-hidden="true">
      <path d="M300 0 Q240 180 200 316 L488 316 L488 0 Z" fill="var(--pale-band)"/>
      <path d="M322 0 Q262 180 226 316 L488 316 L488 0 Z" fill="var(--lime-band)"/>
      <path d="M350 0 Q292 170 258 316 L488 316 L488 0 Z" fill="var(--sun-band)"/>
      <path d="M372 0 Q318 170 290 316 L488 316 L488 0 Z" fill="var(--leaf)"/>
    </svg>

    <div class="brand">
      <span class="brand__dot"></span>
      <span class="brand__name">BRIGHT FURROW</span>
      <span class="brand__tag">LAWN &amp; LANDSCAPE</span>
    </div>

    <ul class="contact">
      <li>Fully Insured</li>
      <li>Dale Ostrov</li>
      <li>410-372-6184</li>
      <li>Dostrov07@quillpost.net</li>
      <li class="contact__web">www.brightfurrow.com</li>
    </ul>
  </section>

  <section class="card card--back" aria-label="Business card back">
    <svg class="card__art" viewBox="0 0 488 316" preserveAspectRatio="none" aria-hidden="true">
      <path d="M0 0 L340 0 Q200 140 0 250 Z" fill="var(--pale-band)"/>
      <path d="M0 0 L310 0 Q180 130 0 226 Z" fill="var(--sun-band)"/>
      <path d="M0 0 L280 0 Q160 115 0 198 Z" fill="var(--lime-band)"/>
      <path d="M0 0 L250 0 Q140 100 0 170 Z" fill="var(--leaf)"/>
    </svg>

    <div class="services">
      <h2 class="services__title">Services we offer:</h2>
      <ul class="services__list">
        <li>Lawn Care &amp; Mowing</li>
        <li>Hedge &amp; Shrub Trimming</li>
        <li>Leaf Removal &amp; Clean Up</li>
        <li>Aeration &amp; Sod</li>
        <li>Mulch &amp; Rock Installations</li>
        <li>Landscape Installations &amp;<br>Renovations</li>
        <li>Commercial Snow Removal</li>
      </ul>
    </div>
  </section>

</main>
</body>
</html>
```